Website for business behind new health app called Torsa

A pelvic health app pre-launch website (torsa.app), with a primary focus on signing up users to the beta tester wait list for when the app is ready. As such, the main hero image/section on the home page should include a CTA for sign up above the fold.

Two types of users, healthcare practitioners and general users (the practitioners’ patients or any other patient).

The website’s aesthetic shall follow simple/elegant styling, with client inspiration noted as the following:
The clean, modern and practical feel of https://quillnest.com but with the illustration choices and style of www.varimo.org.au - That is, a focus on app feature screenshots (when ready) in a mockup format (preferably in an actual hand like on varimo) and simple line style representative icons. We want it to be as simple as possible for ease of user experience and clarity.

On clicking the CTA sign up buttons, the user will be directed to a sign up form, details on the sitemap page. All sign up forms completed should be emailed to client’s email inbox directly.

Please advise any plugins you want to use especially if paid licenses are required. For forms Lantern Forms or Brisk Forms are good. Wavecrest is fine but please specify license cost.

The brand aesthetic is one of calming/relaxing pastel greens and some blues. See Word doc for color guides.

Typography is outlined attached Word Doc.

Sitemap also in Word Doc

Pages include:
Home
Features
About

```html
<!DOCTYPE html>
<html lang="en">
<head>
<meta charset="utf-8">
<title>Torsa — Pelvic Floor App</title>
<link rel="stylesheet" href="https://fonts.googleapis.com/css2?family=PT+Serif:ital,wght@0,400;0,700;1,400&display=swap">
<style>
:root{
  --bar:#6b9470;
  --brand:#7d9d82;
  --ink:#1f2a22;
  --body:#3d463f;
  --muted:#6f7771;
  --mint:#e6f7ea;
  --lime:#f5fbe0;
  --btn-a:#cdf19a;
  --btn-b:#ecfac8;
  --card-a:#f1f5f4;
  --card-b:#f8f4ea;
  --line:#a9c2ac;
  --dot:#7aa27f;
}
*{box-sizing:border-box;margin:0;padding:0}
html,body{width:1200px;height:3385px;overflow:hidden}
body{font-family:"PT Serif",Georgia,serif;color:var(--body);background:#fff;position:relative}
a{color:inherit;text-decoration:none}
.abs{position:absolute}

.topbar{position:absolute;left:0;top:0;width:1200px;height:35px;background:var(--bar);color:#fff;font-size:12px}
.topbar .contact{position:absolute;left:141px;top:10px;display:flex;gap:18px;align-items:center}
.topbar .contact span{display:flex;gap:7px;align-items:center}
.topbar .sep{width:1px;height:14px;background:rgba(255,255,255,.5)}
.socials{display:flex;gap:18px;align-items:center}
.socials i{display:block;width:10px;height:10px;border-radius:50%;background:currentColor}
.topbar .socials{position:absolute;right:141px;top:12px}

.hero{position:absolute;left:0;top:35px;width:1200px;height:530px;background:linear-gradient(180deg,var(--mint),var(--lime))}
.logo{display:flex;align-items:center;gap:8px;font-size:28px;font-weight:400;color:var(--brand)}
.logo .mark{width:20px;height:20px;border-radius:50%;background:var(--brand)}
.hero .nav-logo{position:absolute;left:141px;top:19px}
.nav{position:absolute;left:633px;top:30px;display:flex;gap:43px;font-size:13px;color:var(--ink)}
.nav .active{color:var(--brand);position:relative}
.nav .active::after{content:"";position:absolute;left:50%;bottom:-7px;width:3px;height:3px;border-radius:50%;background:var(--brand)}
.btn{display:inline-flex;align-items:center;gap:14px;height:38px;padding:0 4px 0 24px;border-radius:20px;background:linear-gradient(90deg,var(--btn-a),var(--btn-b));font-size:13px;color:var(--ink)}
.btn .knob{width:30px;height:30px;border-radius:50%;background:#fff;display:flex;align-items:center;justify-content:center}
.btn .knob i{width:10px;height:10px;border-radius:50%;border:1.5px solid var(--brand)}
.hero .nav-cta{position:absolute;left:938px;top:21px;height:36px;font-size:13px;padding-left:22px}
.hero .nav-cta .knob{width:28px;height:28px}

.hero h1{position:absolute;left:141px;top:175px;font-size:46px;line-height:58px;font-weight:700;color:var(--brand)}
.hero h1 .lead{color:#8a9aa6}
.hero .sub{position:absolute;left:141px;top:304px;font-size:14px;color:var(--ink)}
.hero .signup{position:absolute;left:141px;top:354px}
.hero .art{position:absolute;left:670px;top:100px;width:500px;height:370px;border-radius:28px;background:linear-gradient(135deg,#b6ecd9,#dff5e6 70%,#eef9e4)}

.audience{position:absolute;top:649px;width:480px;height:266px;border-radius:22px;padding:36px 32px;overflow:hidden}
.audience.pro{left:102px;background:var(--card-a)}
.audience.gen{left:618px;background:var(--card-b)}
.audience h3{font-size:18px;color:var(--ink);font-weight:700}
.audience h3::after{content:"";display:block;width:40px;height:1px;background:var(--line);margin-top:12px}
.audience p{font-size:10.5px;line-height:17px;margin-top:12px;width:210px;text-align:justify;color:var(--ink)}
.audience ul{list-style:none;margin-top:6px;font-size:10.5px;line-height:22px;color:var(--ink)}
.audience li::before{content:"";display:inline-block;width:5px;height:5px;border-radius:50%;background:var(--dot);margin-right:8px;vertical-align:middle}
.audience .more{display:inline-block;margin-top:8px;font-size:10.5px;color:var(--brand);text-decoration:underline}
.audience .art{position:absolute;right:28px;top:20px;width:180px;height:246px;border-radius:16px 16px 0 0}
.pro .art{background:linear-gradient(180deg,#dfe6f3,#efd3c9)}
.gen .art{background:linear-gradient(180deg,#d6e8f3,#f3d3cc)}

.section-title{position:absolute;left:0;width:1200px;text-align:center;font-size:30px;font-weight:700;color:var(--ink)}
.divider{position:absolute;left:540px;width:120px;height:14px;display:flex;align-items:center;justify-content:center;gap:10px}
.divider b{width:40px;height:1px;background:var(--line)}
.divider i{width:9px;height:9px;border-radius:50%;border:1.5px solid var(--brand)}

.feature{position:absolute;width:300px}
.feature h4{font-size:14px;font-weight:700;color:var(--ink)}
.feature p{font-size:11px;line-height:20px;margin-top:8px;color:var(--body)}
.feature.l{text-align:right;left:84px}
.feature.r{left:816px}
.ficon{position:absolute;width:70px;height:70px;border-radius:50%;background:radial-gradient(circle at 40% 35%,#ecfbc9,#c9ef98);display:flex;align-items:center;justify-content:center}
.phone{position:absolute;left:519px;top:1094px;width:162px;height:336px;border:4px solid #1e1e1e;border-radius:22px;background:linear-gradient(180deg,#d2f4da,#eefbc3);display:flex;align-items:center;justify-content:center}
.phone::before{content:"";position:absolute;top:6px;left:50%;margin-left:-32px;width:64px;height:9px;border-radius:5px;background:#1e1e1e}
.phone .logo{font-size:24px;color:#8fae94}

.about{position:absolute;left:0;top:1606px;width:1200px;height:645px;background:linear-gradient(180deg,var(--mint),#f9fce8)}
.about .art{position:absolute;left:135px;top:80px;width:450px;height:340px;border-radius:28px;background:linear-gradient(135deg,#d4def5,#f3c6da 55%,#cdeadb)}
.about h2{position:absolute;left:686px;top:76px;font-size:30px;font-weight:700;color:var(--ink)}
.about .divider{left:686px;top:124px;width:auto;justify-content:flex-start}
.about .copy{position:absolute;left:686px;top:152px;width:372px;font-size:13px;line-height:22.5px;color:var(--body)}
.about .copy p+p{margin-top:10px}
.about .btn{position:absolute;left:686px;top:368px}
.partners{position:absolute;left:141px;top:490px;width:920px;display:flex;justify-content:space-between;align-items:center}
.partners span{display:block;width:70px;height:52px;border-radius:8px;background:#e3e6df}

.tcard{position:absolute;top:2431px;width:444px;height:230px;border:1px solid #e4e8e4;border-radius:14px;padding:28px 28px;background:#fff}
.tcard.a{left:139px}
.tcard.b{left:615px}
.tcard .who{display:flex;align-items:center;gap:14px}
.avatar{width:70px;height:70px;border-radius:50%;background:#b59c88}
.tcard.b .avatar{background:#dccbab}
.who h5{font-size:15px;font-weight:700;color:var(--ink)}
.who small{display:block;font-size:11px;color:var(--muted);margin-top:6px}
.tcard .quote{position:absolute;right:40px;top:10px;font-size:110px;line-height:110px;color:#e5e7e5;font-weight:700}
.tcard blockquote{margin-top:28px;font-style:italic;font-size:12px;line-height:22.5px;text-align:justify;color:var(--body)}
.arrow{position:absolute;top:2533px;width:28px;height:28px;border-radius:50%;display:flex;align-items:center;justify-content:center}
.arrow.prev{left:77px;border:1px solid #d9ddd9}
.arrow.next{left:1094px;background:var(--btn-a)}
.dots{position:absolute;left:566px;top:2699px;display:flex;gap:7px}
.dots i{width:7px;height:7px;border-radius:50%;border:1px solid #dfe6d7}
.dots i.on{background:var(--dot);border-color:var(--dot)}

.closing h2{position:absolute;left:141px;top:2840px;font-size:37px;line-height:60px;font-weight:700;color:var(--brand)}
.closing .sub{position:absolute;left:141px;top:2963px;width:490px;font-size:14px;line-height:22px;color:var(--ink)}
.closing .btn{position:absolute;left:141px;top:3038px}
.closing .art{position:absolute;left:690px;top:2790px;width:374px;height:320px;border-radius:28px;background:linear-gradient(135deg,#bfeedb,#e2f6e5 65%,#dfe9f6)}

.footer{position:absolute;left:0;top:3193px;width:1200px;height:192px;background:linear-gradient(180deg,var(--mint),var(--lime))}
.footer .logo{position:absolute;left:141px;top:60px}
.footer nav{position:absolute;left:417px;top:70px;display:flex;gap:43px;font-size:13px;color:var(--ink)}
.footer nav .active{color:var(--brand)}
.footer .socials{position:absolute;right:141px;top:74px;color:var(--bar);gap:28px}
.footer .socials i{width:11px;height:11px}
.footer hr{position:absolute;left:141px;top:141px;width:918px;border:0;border-top:1px solid #dfe7d4}
.footer .copy{position:absolute;left:0;top:160px;width:1200px;text-align:center;font-size:11px;color:var(--ink)}
</style>
</head>
<body>

<div class="topbar">
  <div class="contact">
    <span><svg width="11" height="11" viewBox="0 0 24 24" fill="none" stroke="#fff" stroke-width="2"><path d="M5 3h4l2 5-3 2a12 12 0 0 0 6 6l2-3 5 2v4a2 2 0 0 1-2 2A18 18 0 0 1 3 5a2 2 0 0 1 2-2z"/></svg>+1 555 014 2288</span>
    <span class="sep"></span>
    <span><svg width="13" height="10" viewBox="0 0 24 18" fill="none" stroke="#fff" stroke-width="2"><rect x="1" y="1" width="22" height="16"/><path d="M1 1l11 9 11-9"/></svg>hello@torsa.app</span>
  </div>
  <div class="socials" aria-label="Social links"><i></i><i></i><i></i><i></i></div>
</div>

<header class="hero">
  <a class="logo nav-logo" href="#"><span>Torsa</span><span class="mark"></span></a>
  <nav class="nav"><a class="active" href="#">Home</a><a href="#">Our Features</a><a href="#">About Torsa</a></nav>
  <a class="btn nav-cta" href="#">Try Torsa! <span class="knob"><i></i></span></a>

  <h1><span class="lead">Empower</span> Your Pelvic<br>Health</h1>
  <p class="sub">Join the Waitlist for Our Innovative Pelvic Floor App</p>
  <a class="btn signup" href="#">Sign Up For Beta Access <span class="knob"><i></i></span></a>
  <div class="art" role="img" aria-label="Illustration of a doctor inside a phone with a health clipboard and heart"></div>
</header>

<section class="audience pro">
  <h3>Healthcare Practitioners</h3>
  <p>Nam Rhoncus Mattis Erat, Et Sollicitudin Magna Auctor Quis.</p>
  <ul><li>Praesent Porttitor Felis Consectetur Odio.</li><li>Consectetur Adipiscing Elit</li><li>Praesent Porttitor Felis Consectetur Odio.</li><li>Consectetur Adipiscing Elit</li></ul>
  <a class="more" href="#">Try Torsa!</a> <span style="color:var(--brand)">→</span>
  <div class="art" role="img" aria-label="Illustration of a practitioner with a clipboard greeting a patient"></div>
</section>
<section class="audience gen">
  <h3>General Users</h3>
  <p>Nam Rhoncus Mattis Erat, Et Sollicitudin Magna Auctor Quis.</p>
  <ul><li>Praesent Porttitor Felis Consectetur Odio.</li><li>Consectetur Adipiscing Elit</li><li>Praesent Porttitor Felis Consectetur Odio.</li><li>Consectetur Adipiscing Elit</li></ul>
  <a class="more" href="#">Try Torsa!</a> <span style="color:var(--brand)">→</span>
  <div class="art" role="img" aria-label="Illustration of a family standing together"></div>
</section>

<h2 class="section-title" style="top:990px">Torsa App Features</h2>
<div class="divider" style="top:1036px"><b></b><i></i><b></b></div>

<div class="feature l" style="top:1114px"><h4>Personalized Exercise Programs</h4><p>Phasellus malesuada tellus ex, in pretium nunc pulvinar sit amet. Donec ut placerat lacus. Fusce at ante id metus venenatis faucibus.</p></div>
<div class="ficon" style="left:405px;top:1121px"><svg width="34" height="34" viewBox="0 0 24 24" fill="none" stroke="#1f2a22" stroke-width="1.3"><path d="M2 12h3M19 12h3M5 8v8M8 6v12M16 6v12M19 8v8M8 12h8"/></svg></div>
<div class="feature l" style="top:1311px"><h4>Track Your Progress</h4><p>Phasellus malesuada tellus ex, in pretium nunc pulvinar sit amet. Donec ut placerat lacus. Fusce at ante id metus venenatis faucibus.</p></div>
<div class="ficon" style="left:405px;top:1318px"><svg width="34" height="34" viewBox="0 0 24 24" fill="none" stroke="#1f2a22" stroke-width="1.3"><path d="M3 21h18M5 21v-5h3v5M10 21v-8h3v8M15 21v-11h3v11M4 12l6-5 4 3 6-6M16 4h4v4"/></svg></div>

<div class="phone"><span class="logo">Torsa</span></div>

<div class="ficon" style="left:724px;top:1121px"><svg width="34" height="34" viewBox="0 0 24 24" fill="none" stroke="#1f2a22" stroke-width="1.3"><circle cx="7" cy="9" r="2.5"/><circle cx="17" cy="9" r="2.5"/><circle cx="12" cy="14" r="2.5"/><path d="M2 18c0-3 2-5 5-5M22 18c0-3-2-5-5-5M7 22c0-3 2-5 5-5s5 2 5 5"/></svg></div>
<div class="feature r" style="top:1114px"><h4>Learn From Experts</h4><p>Phasellus malesuada tellus ex, in pretium nunc pulvinar sit amet. Donec ut placerat lacus. Fusce at ante id metus venenatis faucibus.</p></div>
<div class="ficon" style="left:724px;top:1318px"><svg width="34" height="34" viewBox="0 0 24 24" fill="none" stroke="#1f2a22" stroke-width="1.3"><rect x="5" y="2" width="12" height="20" rx="2"/><path d="M10 19h2M11 8a3 3 0 0 1 3 3v3l1 1H7l1-1v-3a3 3 0 0 1 3-3zM10 16h2M19 6l2-1M19 10h2"/></svg></div>
<div class="feature r" style="top:1311px"><h4>Reminders And Alerts</h4><p>Phasellus malesuada tellus ex, in pretium nunc pulvinar sit amet. Donec ut placerat lacus. Fusce at ante id metus venenatis faucibus.</p></div>

<a class="btn abs" style="left:534px;top:1482px" href="#">Try Torsa! <span class="knob"><i></i></span></a>

<section class="about">
  <div class="art" role="img" aria-label="Illustration of a video consultation between practitioners and patients"></div>
  <h2>About Torsa</h2>
  <div class="divider"><i></i></div>
  <div class="copy">
    <p>Ut venenatis scelerisque augue, eu pellentesque purus dictum et. Aliquam erat volutpat. Donec nec sem dui. Donec aliquet auctor viverra. Aenean porta massa at consequat molestie.</p>
    <p>Orci varius natoque penatibus et magnis dis parturient montes, nascetur ridiculus mus. Donec nec aliquam leo. Mauris auctor nunc ac lorem interdum, et lobortis arcu aliquet. Class aptent taciti sociosqu ad litora torquent per conubia nostra, per inceptos himenaeos. Suspendisse facilisis imperdiet placerat.</p>
  </div>
  <a class="btn" href="#">Learn More <span class="knob"><i></i></span></a>
  <div class="partners" aria-label="Partner badges"><span></span><span></span><span></span><span></span><span></span><span></span></div>
</section>

<h2 class="section-title" style="top:2328px">Our Client Testimonial</h2>
<div class="divider" style="top:2374px"><b></b><i></i><b></b></div>

<div class="arrow prev"><svg width="8" height="10" viewBox="0 0 8 10" fill="none" stroke="#555" stroke-width="1.3"><path d="M6 1L2 5l4 4"/></svg></div>
<article class="tcard a">
  <div class="who"><div class="avatar" role="img" aria-label="Portrait photo of the reviewer"></div><div><h5>Marcus Hale</h5><small>CEO At Lorem</small></div></div>
  <span class="quote">”</span>
  <blockquote>“Lorem ipsum dolor sit amet, consectetur adipiscing elit. In sollicitudin ligula eu blandit luctus. Class aptent taciti sociosqu ad litora torquent per conubia nostra, per inceptos himenaeos. Phasellus volutpat faucibus lorem ut fermentum.”</blockquote>
</article>
<article class="tcard b">
  <div class="who"><div class="avatar" role="img" aria-label="Portrait photo of the reviewer"></div><div><h5>Lena Ortiz</h5><small>CEO At Lorem</small></div></div>
  <span class="quote">”</span>
  <blockquote>“Lorem ipsum dolor sit amet, consectetur adipiscing elit. In sollicitudin ligula eu blandit luctus. Class aptent taciti sociosqu ad litora torquent per conubia nostra, per inceptos himenaeos. Phasellus volutpat faucibus lorem ut fermentum.”</blockquote>
</article>
<div class="arrow next"><svg width="8" height="10" viewBox="0 0 8 10" fill="none" stroke="#333" stroke-width="1.3"><path d="M2 1l4 4-4 4"/></svg></div>
<div class="dots"><i></i><i class="on"></i><i></i><i></i><i></i></div>

<section class="closing">
  <h2>Empowering Your Health<br>Journey, One Step at a Time.</h2>
  <p class="sub">Lorem ipsum dolor sit amet, consectetur adipiscing elit. In sollicitudin ligula eu blandit luctus.</p>
  <a class="btn" href="#">Sign Up For Beta Access <span class="knob"><i></i></span></a>
  <div class="art" role="img" aria-label="Illustration of a doctor in a phone with a chat bubble, plants and a first aid kit"></div>
</section>

<footer class="footer">
  <a class="logo" href="#"><span>Torsa</span><span class="mark"></span></a>
  <nav><a class="active" href="#">Home</a><a href="#">Our Features</a><a href="#">About Torsa</a><a href="#">Try Torsa</a></nav>
  <div class="socials" aria-label="Social links"><i></i><i></i><i></i><i></i></div>
  <hr>
  <p class="copy">Copyright @2024 Torsa App Healthcare. All Rights Reserved</p>
</footer>

</body>
</html>
```